1/2 Page add for BRMTL Conference

We are looking for a 1/2 page ad to support the annual BRMTL conference. I want to encourage the attendees to come to our both so we can explain how they can save money on food and supplies. here is a link to the conference. https://www.brmtl-example.org/conference/ here is our website www.pantrywisehub-example.com - the what we do can be captured in the ad. We will be at booth 505. Our goal is to get people to our booth #505 to explain the services that we provide –

Discounted food pricing
Free menu planning/design
Use of Registered Dietitian
Huge selection of discounted PPE and other necessary supplies to run any child care center

We have over 6000 members in 46 States and work with both small and large food distributors. We have been a sponsor of the association for the last 10 years.

Target Market(s)

Child care centers

Requirements
Must have
• Booth number -outline of what we do --- Stress we are a FREE service getting our members reduced pricing on food and supplies

```html
<!DOCTYPE html>
<html lang="en">
<head>
<meta charset="utf-8">
<title>Annual BRMTL Conference – PantryWise Hub</title>
<link rel="stylesheet" href="https://fonts.googleapis.com/css2?family=Oswald:wght@400;500;600;700&family=Open+Sans:wght@400;600;700&display=swap">
<style>
  :root{
    --blue:#2f80c3;
    --blue-dark:#1d5f9a;
    --navy:#18324f;
    --green:#a6d36d;
    --green-dark:#7fbf4d;
    --ink:#27384a;
    --white:#ffffff;
    --paper:#f3f6f9;
  }
  *{box-sizing:border-box;margin:0;padding:0}
  html,body{width:878px;height:1200px;overflow:hidden;background:var(--white)}
  body{font-family:"Open Sans",Arial,sans-serif;color:var(--ink)}
  .ad{position:relative;width:878px;height:1200px;overflow:hidden;background:var(--white)}

  .hero-photo{position:absolute;left:0;top:0;width:878px;height:560px;
    background:linear-gradient(135deg,#1b3a5e 0%,#24507e 45%,#3a6a8f 70%,#8a6a48 100%)}
  .hero-shade{position:absolute;left:0;top:0;width:878px;height:560px;
    background:linear-gradient(90deg,rgba(16,36,60,.75) 0%,rgba(16,36,60,.35) 60%,rgba(16,36,60,0) 100%)}

  .title-frame{position:absolute;left:160px;top:72px;width:558px;height:200px;border:3px solid var(--white);border-bottom:none}
  .title-annual{position:absolute;left:0;width:878px;top:92px;text-align:center;
    font-family:"Oswald",Arial,sans-serif;font-weight:500;font-size:74px;letter-spacing:4px;color:var(--white)}
  .title-event{position:absolute;left:0;width:878px;top:182px;text-align:center;
    font-family:"Oswald",Arial,sans-serif;font-weight:500;font-size:46px;letter-spacing:2px;color:var(--white)}
  .question-banner{position:absolute;left:200px;top:250px;width:576px;height:50px;background:var(--blue);
    border:2px solid var(--white);display:flex;align-items:center;justify-content:center;
    font-family:"Oswald",Arial,sans-serif;font-size:26px;letter-spacing:1px;color:var(--white)}

  .angle-art{position:absolute;left:0;top:500px}

  .services-tab{position:absolute;left:0;top:578px;width:300px;height:62px;}
  .services-tab span{position:absolute;left:28px;top:4px;font-family:"Oswald",Arial,sans-serif;font-weight:500;font-size:42px;color:var(--white);letter-spacing:1px}
  .services-list{position:absolute;left:28px;top:660px;list-style:none;width:420px}
  .services-list li{position:relative;padding-left:28px;font-size:18px;line-height:25px;color:var(--ink);margin-bottom:3px}
  .services-list svg{position:absolute;left:0;top:5px}

  .join{position:absolute;left:560px;top:582px;width:300px;text-align:center;color:var(--white);font-family:"Oswald",Arial,sans-serif}
  .join-big{font-size:48px;font-weight:500;line-height:50px;letter-spacing:2px}
  .join-small{font-size:30px;line-height:36px;letter-spacing:1px}
  .join-url{position:absolute;left:576px;top:688px;width:284px;height:38px;background:var(--white);
    display:flex;align-items:center;justify-content:center;font-size:14px;color:var(--ink)}
  .join-booth{position:absolute;left:576px;top:734px;width:284px;height:36px;background:var(--blue-dark);
    display:flex;align-items:center;justify-content:center;font-size:15px;font-weight:600;color:var(--white)}

  .partner-name{position:absolute;left:36px;top:838px;width:300px;display:flex;align-items:center;gap:12px;
    font-family:"Oswald",Arial,sans-serif;font-weight:700;font-size:30px;line-height:32px;color:var(--navy)}
  .partner-name .dot{flex:0 0 46px;height:46px;border-radius:50%;background:var(--navy)}
  .brand-name{position:absolute;left:430px;top:860px;display:flex;align-items:center;gap:14px;
    font-family:"Oswald",Arial,sans-serif;font-weight:500;font-size:44px;color:var(--blue-dark)}
  .brand-name .square{width:46px;height:46px;background:var(--green-dark)}

  .about{position:absolute;left:40px;top:950px;width:798px;text-align:center;font-size:22px;line-height:32px;color:var(--ink)}
  .about strong{color:var(--blue);font-weight:700}

  .footer-art{position:absolute;left:0;top:1060px}
  .footer-cta{position:absolute;left:24px;top:1118px;font-family:"Oswald",Arial,sans-serif;font-weight:500;font-size:26px;color:var(--navy);letter-spacing:1px}
  .footer-url{position:absolute;left:430px;top:1120px;font-family:"Oswald",Arial,sans-serif;font-size:25px;color:var(--white);letter-spacing:1px}
</style>
</head>
<body>
<main class="ad">
  <div class="hero-photo" role="img" aria-label="Groceries and supplies on a dark blue wooden table: cooking oil, paper towels, apples and pantry goods"></div>
  <div class="hero-shade"></div>

  <div class="title-frame"></div>
  <h1 class="title-annual">ANNUAL</h1>
  <h2 class="title-event">BRMTL CONFERENCE</h2>
  <p class="question-banner">WANT TO SAVE MONEY ON FOOD &amp; SUPPLIES?</p>

  <svg class="angle-art" width="878" height="300" viewBox="0 0 878 300" aria-hidden="true">
    <polygon points="0,60 878,40 878,300 0,300" fill="#ffffff"/>
    <polygon points="0,75 300,72 300,140 0,140" fill="#2f80c3"/>
    <polygon points="300,72 316,106 300,140" fill="#1d5f9a"/>
    <polygon points="540,86 878,40 878,282 540,282" fill="#2f80c3"/>
    <polygon points="540,86 570,86 540,120" fill="#1d5f9a"/>
  </svg>

  <div class="services-tab"><span>SERVICES</span></div>
  <ul class="services-list">
    <li><svg width="16" height="14" viewBox="0 0 16 14"><path d="M1 7l5 5 9-11" fill="none" stroke="#2f80c3" stroke-width="3"/></svg>Discounted food pricing.</li>
    <li><svg width="16" height="14" viewBox="0 0 16 14"><path d="M1 7l5 5 9-11" fill="none" stroke="#2f80c3" stroke-width="3"/></svg>Free menu planning/design.</li>
    <li><svg width="16" height="14" viewBox="0 0 16 14"><path d="M1 7l5 5 9-11" fill="none" stroke="#2f80c3" stroke-width="3"/></svg>Use of Registered Dietitian.</li>
    <li><svg width="16" height="14" viewBox="0 0 16 14"><path d="M1 7l5 5 9-11" fill="none" stroke="#2f80c3" stroke-width="3"/></svg>Huge selection of discounted PPE &amp; other necessary supplies to run any child care center.</li>
  </ul>

  <div class="join">
    <p class="join-big">JOIN</p>
    <p class="join-small">OUR CONFERENCE</p>
  </div>
  <p class="join-url">https://www.brmtl-example.org/conference/</p>
  <p class="join-booth">Meet Us At Booth #505</p>

  <div class="partner-name"><span class="dot"></span><span>NATIONAL BRMTL<br>SPONSORS GROUP</span></div>
  <div class="brand-name"><span class="square"></span><span>PantryWise Hub</span></div>

  <p class="about">We have over <strong>6000</strong> members in <strong>46</strong> States and work with both small and large food distributors. We have been a <strong>sponsor of the association for the last 10 years.</strong></p>

  <svg class="footer-art" width="878" height="140" viewBox="0 0 878 140" aria-hidden="true">
    <polygon points="0,40 340,40 380,110 0,110" fill="#a6d36d"/>
    <polygon points="380,50 878,50 878,110 350,110" fill="#2f80c3"/>
    <polygon points="0,110 878,110 878,140 0,140" fill="#ffffff"/>
    <polygon points="0,110 220,110 180,140 0,140" fill="#7fbf4d"/>
    <polygon points="700,110 878,110 878,140 740,140" fill="#1d5f9a"/>
  </svg>
  <p class="footer-cta">GET IN TOUCH WITH US</p>
  <p class="footer-url">WWW.PANTRYWISEHUB-EXAMPLE.COM</p>
</main>
</body>
</html>
```